Zippy Festivities!!! New business idea looking for proof of concept among customers

PERSONAL, FUN, EXCITING, MEMORABLE, UNIQUE
this is the idea for the business so I would like the brochure to portray this as well
I would like an eye catching design. The concept of the business is simple. We want to provide a personalized, memorable, unique and enjoyable experience and celebration for our clients as they chose to celebrate different events which may include but are not limited to (Birthday, holiday, anniversary, Special Event, no reason) for whomever it may be (friend, family member, significant other, coworker, frat/sorority brother/sister, etc) at a location of their choosing (on campus, public park, restaurant, bar etc). The celebration can take place at a private location or in a public scene where strangers can look on and take part in the fun. We will catch this act on video as well as take personalized photos and share it with the client for their own personal memories as well as utilize it on our own social media platforms. There are different packages that i would like to be included and most of the information id like to be included is attached. However, I would like to be able to add information or discard as necessary. The logo I would like to use is attached as well in three different designs. Designers may utilize the logo that they see fits their personal design the best! the logo with the flash in the background is one I personally like most but I am open to anything.
Just for visual of the concept. you want to surprise your friend with a Birthday blowout package for their birthday. The two of you are walking to class when your friend is shouted out by a DJ using a portable pa speaker system. Suddenly two confetti cannons go off, and your friend is overwhelmed with attention as well as personalized gifts given by strangers. Your friend as well as all onlookers are baffled to learn that you set up the whole experience just for them. Photos and videos have been taken throughout the whole experience to be shared with friends who weren't able to be their in person.
Designers you have the opportunity to be a part of a new, exciting and fun business. More than likely I will need a lot of things designed for the future of this business and I am looking to potentially develop a long-term partnership.
Target Market(s)
Ages 18-35. College students, Couples, office workers. Anybody celebrating anything.
Industry/Entity Type
Business
Requirements
Must have
- visuals that capture the attention of those viewing the brochure as well as providing a clear explanation of the concepts and packages. Packages must be easy to edit as pricing is not finalized. I would like the different packages to be on different pages with corresponding pictures in the panels or as background that still fit the overall theme. When you open the brochure the three panels should be Birthdays, Anniversaries, Other events, each with corresponding information from attached document

```html
<!DOCTYPE html>
<html lang="en">
<head>
<meta charset="utf-8">
<title>Zippy Festivities – Trifold Brochure</title>
<link rel="stylesheet" href="https://fonts.googleapis.com/css2?family=Kalam:wght@700&family=Montserrat:wght@400;600;700&family=Oswald:wght@500&family=Roboto+Condensed:wght@400&display=swap">
<style>
:root{
  --page:#ececef;
  --blue:#3347e6;
  --blue-bright:#2f6dff;
  --cyan:#4fd0ff;
  --violet:#4a2fd2;
  --violet-deep:#2a1a9c;
  --pink:#ff2fae;
  --ink:#333;
  --grey:#e3e3e8;
  --white:#fff;
  --hand:"Kalam",cursive;
  --sans:"Montserrat",sans-serif;
  --cond:"Roboto Condensed",sans-serif;
  --tall:"Oswald",sans-serif;
}
*{box-sizing:border-box;margin:0;padding:0}
html,body{width:1200px;height:1200px;overflow:hidden;background:var(--page)}
.sheet{position:absolute;left:253px;width:694px;height:540px;overflow:hidden;background:var(--white)}
.sheet--outside{top:51px}
.sheet--inside{top:614px}
.panel{position:absolute;top:0;height:100%;width:232px;overflow:hidden}
.panel--1{left:0}.panel--2{left:232px;width:231px}.panel--3{left:463px;width:231px}
.photo{position:absolute;border-radius:50%;border:4px solid var(--white);z-index:2}
.hand{font-family:var(--hand);font-weight:700}

/* outside: intro panel */
.intro{background:linear-gradient(90deg,#fff 0%,#f2f2f5 60%,var(--grey) 100%)}
.intro__title{position:absolute;left:19px;top:16px;font-size:20px;color:var(--blue)}
.intro__text{position:absolute;left:19px;top:48px;width:202px;font:400 7.3px/10.3px var(--sans);color:var(--ink);text-align:justify}
.intro__swoosh{position:absolute;left:0;top:200px;width:232px;height:70px}
.intro__ask{position:absolute;left:19px;top:282px;width:205px;font:700 8.6px/11px var(--sans);color:var(--blue)}
.form{position:absolute;left:19px;top:322px;width:200px;list-style:none}
.form li{display:flex;font:400 7.8px/1 var(--sans);color:#444;height:20.6px;align-items:flex-end}
.form li span{flex:1;border-bottom:1px dotted #777;margin-left:4px;margin-bottom:1px}
.intro__note{position:absolute;left:19px;top:493px;width:205px;font:italic 700 7.6px/10.5px var(--sans);color:var(--blue)}

/* outside: middle panel */
.blast{background:linear-gradient(180deg,var(--violet) 0%,#3b2cd0 60%,var(--blue-bright) 100%)}
.blast__top{position:absolute;inset:0}
.blast__tag{position:absolute;top:14px;left:0;width:231px;text-align:center;font-size:16px;line-height:19px;color:var(--blue-bright)}
.blast__scene{position:absolute;left:0;top:222px;width:231px;height:160px;background:linear-gradient(135deg,#6b2bd8,#d23ab8 45%,#2fa7e8)}
.contact{position:absolute;left:20px;top:412px;color:var(--white)}
.contact__name{font-size:19px;line-height:24px;color:var(--white)}
.contact__row{display:flex;align-items:center;gap:6px;font:400 10.2px/12.6px var(--sans)}
.contact__row svg{width:8px;height:8px;flex:none}
.contact__gap{height:10px}

/* outside: cover panel */
.cover{background:linear-gradient(180deg,#3a2ad6 0%,var(--violet-deep) 100%)}
.cover__burst{position:absolute;left:0;top:0;width:231px;height:150px;background:radial-gradient(ellipse at 58% 32%,#fff 0%,#c9c4ff 14%,#6d5cf0 40%,#3a2ad6 75%)}
.cover__name{position:absolute;top:40px;left:0;width:231px;text-align:center;font-size:27px;line-height:30px;color:var(--white)}
.cover__scene{position:absolute;left:0;top:128px;width:231px;height:340px;background:linear-gradient(160deg,#1d3fb8,#c42fb0 45%,#ff4ab8 65%,#2a1a9c)}
.cover__wave{position:absolute;left:0;top:118px;width:231px;height:40px}
.traits{position:absolute;left:0;top:200px;list-style:none}
.traits li{font-size:17px;line-height:19px;color:var(--white);padding:3px 12px 5px 12px;margin-bottom:13px;background:linear-gradient(90deg,rgba(255,47,174,.85),rgba(255,47,174,.55));width:max-content}
.cover__bottom{position:absolute;left:0;bottom:0;width:231px;height:120px}
.cover__cta{position:absolute;left:17px;top:432px;color:var(--white);font:500 16px/18px var(--tall);text-transform:uppercase;transform:scaleX(.88);transform-origin:left}
.cover__phone{position:absolute;left:17px;top:469px;font:700 24px/26px var(--sans);color:var(--cyan)}
.cover__url{position:absolute;left:17px;top:494px;font:400 10.4px/12px var(--sans);color:var(--white)}
.cover__social{position:absolute;left:17px;top:511px;display:flex;align-items:center;gap:6px;font:400 10.4px/12px var(--sans);color:var(--white)}
.cover__social i{width:9px;height:9px;background:var(--cyan);display:block}

/* inside: packages */
.pkgs{padding:18px 12px 0 19px}
.pkgs--light{background:linear-gradient(90deg,#fff,#f4f4f7)}
.pkgs--dark{background:linear-gradient(180deg,var(--violet) 0%,#3a2cd4 100%);color:var(--white)}
.pkgs__title{position:relative;z-index:1;font-size:16px;line-height:20px;color:var(--blue)}
.pkgs--dark .pkgs__title{color:var(--white)}
.pkgs__sub{font:400 5.6px/8px var(--cond);color:#555}
.pkgs--dark .pkgs__sub{color:#dcdcff}
.pkgs__kinds{font-size:11px;line-height:13px;color:var(--blue)}
.pkg{position:relative;z-index:1;margin-top:15px}
.pkg__name{font-size:14px;line-height:17px;color:var(--blue-bright);margin-bottom:3px;white-space:nowrap}
.pkgs--dark .pkg__name{color:var(--cyan)}
.pkg__name b{color:var(--blue)}
.pkgs--dark .pkg__name b{color:var(--white)}
.pkg ul{list-style:none;font:400 5.8px/9.2px var(--cond);color:#333}
.pkgs--dark .pkg ul{color:#eceaff}
.pkg li{position:relative;padding-left:7px}
.pkg li::before{content:"";position:absolute;left:1px;top:3.6px;width:2.6px;height:2.6px;border-radius:50%;background:var(--blue-bright)}
.pkgs--dark .pkg li::before{background:var(--cyan)}
.pkg li.note{padding-left:11px}
.pkg li.note::before{display:none}
.kinds{display:grid;grid-template-columns:1fr 1fr;font:400 5.6px/8.6px var(--cond);color:#333;list-style:none;margin-top:5px}
.kinds li{position:relative;padding-left:6px}
.kinds li::before{content:"";position:absolute;left:0;top:3.2px;width:2.4px;height:2.4px;border-radius:50%;background:var(--blue-bright)}
.pkg--inset{padding-left:78px;margin-left:-19px}
.pkg--inset .pkg__name{margin-left:-30px;font-size:13.5px}
.balloons{position:absolute;left:0;top:278px;width:80px;height:150px;z-index:0;background:radial-gradient(circle at 45% 18%,#ff5aa8 0 14%,transparent 15%),radial-gradient(circle at 22% 42%,#3fa8ff 0 15%,transparent 16%),radial-gradient(circle at 62% 58%,#ffd23a 0 13%,transparent 14%),radial-gradient(circle at 30% 78%,#5ad35a 0 13%,transparent 14%);opacity:.9}
.wave{position:absolute;left:0;bottom:0;width:232px;height:120px}
</style>
</head>
<body>

<!-- Outside of the trifold -->
<section class="sheet sheet--outside">

  <div class="panel panel--1 intro">
    <h2 class="intro__title hand">What We Do :</h2>
    <p class="intro__text">Imagine a suprise party that comes to you. IT'S HERE! At Zippy Festivities it is our goal to provide a personalized, exciting, fun, memorable, and unique celebration and experience for all of our clients. We want to provide the surprise that will make someone close to you feel SPECIAL and help in bringing every celebratory vision to life. When you have a reason to celebrate, nothing should be off limits! We will catch this act on video as well as take personalized photos for our clients to share and relive the celebration. Our team will go above and beyond to exceed all of our clients expectations as they celebrate EVERY occasion. We know how to make ANY CELEBRATION a BLAST in a FLASH.</p>
    <svg class="intro__swoosh" viewBox="0 0 232 70" preserveAspectRatio="none" aria-hidden="true">
      <path d="M0 22 C70 40 150 30 232 10 L232 52 C150 58 80 60 0 48Z" fill="#3b2cd6"/>
      <path d="M0 30 C80 50 160 40 232 22 L232 34 C160 52 80 58 0 42Z" fill="#6f8cff" opacity=".7"/>
      <path d="M0 46 C80 58 150 56 232 46 L232 54 C150 62 80 64 0 54Z" fill="#9fb4ff" opacity=".6"/>
    </svg>
    <p class="intro__ask">Upon contacting Zippy Festivities customers must be able to provide the following information :</p>
    <ul class="form">
      <li>Customer Name:<span></span></li>
      <li>Event Type:<span></span></li>
      <li>Package:<span></span></li>
      <li>Delivery Type:<span></span></li>
      <li>Date/Time:<span></span></li>
      <li>Location:<span></span></li>
      <li>Additional notes:<span></span></li>
      <li>Approximate Price budget:<span></span></li>
    </ul>
    <p class="intro__note">Please contact us with any questions you may have and we will be happy to answer them.</p>
  </div>

  <div class="panel panel--2 blast">
    <div class="blast__scene" role="img" aria-label="Photo of a crowd celebrating under falling confetti"></div>
    <svg class="blast__top" viewBox="0 0 231 540" preserveAspectRatio="none" aria-hidden="true">
      <path d="M0 0 H222 C215 90 160 200 60 250 C40 258 20 262 0 262Z" fill="#fff"/>
      <path d="M222 0 H231 V40 C222 140 170 220 70 262 L60 250 C160 200 215 90 222 0Z" fill="#5a9bff"/>
    </svg>
    <p class="blast__tag hand">we make any<br>CELEBRATION a blast<br>in a FLASH</p>
    <div class="photo" style="left:70px;top:80px;width:130px;height:130px;background:linear-gradient(140deg,#ffd1e8,#ff4fa8 55%,#6a3ad0)" role="img" aria-label="Photo of friends posing with party props"></div>
    <div class="photo" style="left:22px;top:176px;width:128px;height:128px;background:linear-gradient(140deg,#5a3cc8,#e43aa6 50%,#f2b07a)" role="img" aria-label="Photo of masked party guests toasting"></div>
    <div class="contact">
      <h3 class="contact__name hand">Zippy Festivities</h3>
      <p class="contact__row"><svg viewBox="0 0 10 10"><path d="M2 1 L4 1 L4.6 3.2 L3.4 4 C4 5.4 4.6 6 6 6.6 L6.8 5.4 L9 6 L9 8 C5 8.6 1.4 5 2 1Z" fill="#fff"/></svg>555-010-0199</p>
      <p class="contact__row"><svg viewBox="0 0 10 10"><circle cx="5" cy="5" r="4" fill="none" stroke="#fff"/><path d="M1 5 H9 M5 1 C3 3 3 7 5 9 C7 7 7 3 5 1" fill="none" stroke="#fff" stroke-width=".7"/></svg>www.ZippyFestivities.com</p>
      <p class="contact__row"><svg viewBox="0 0 10 10"><rect x="1" y="2" width="8" height="6" fill="#fff"/><path d="M1 2 L5 5.5 L9 2" fill="none" stroke="#3a2cd4" stroke-width=".8"/></svg>ZippyFestivities@mailbox.com</p>
      <div class="contact__gap"></div>
      <p class="contact__row"><svg viewBox="0 0 10 10"><rect x="1" y="1" width="8" height="8" fill="#fff"/></svg>ZippyFestivities</p>
      <p class="contact__row"><svg viewBox="0 0 10 10"><rect x="1" y="1" width="8" height="8" fill="none" stroke="#fff"/></svg>ZippyFestivities</p>
    </div>
  </div>

  <div class="panel panel--3 cover">
    <div class="cover__burst"></div>
    <h1 class="cover__name hand">Zippy<br>Festivities</h1>
    <div class="cover__scene" role="img" aria-label="Photo of a young woman cheering under colourful confetti"></div>
    <svg class="cover__wave" viewBox="0 0 231 40" preserveAspectRatio="none" aria-hidden="true">
      <path d="M0 0 H231 V4 C160 0 90 30 0 22Z" fill="#3a2ad6"/>
      <path d="M0 22 C90 30 160 0 231 4 V10 C160 8 90 36 0 28Z" fill="#4fd0ff"/>
    </svg>
    <ul class="traits hand">
      <li>Personalized</li><li>Fun</li><li>Exciting</li><li>Memorable</li><li>Unique</li>
    </ul>
    <svg class="cover__bottom" viewBox="0 0 231 120" preserveAspectRatio="none" aria-hidden="true">
      <path d="M0 10 C60 30 150 10 231 -10 V120 H0Z" fill="#3a2cd4"/>
      <path d="M120 18 C170 10 205 0 231 -6 V6 C200 14 170 20 120 18Z" fill="#4fd0ff" opacity=".8"/>
    </svg>
    <p class="cover__cta">Plan your<br>celebration today!</p>
    <p class="cover__phone">555-010-0199</p>
    <p class="cover__url">www.ZippyFestivities.com</p>
    <p class="cover__social"><i></i>@zippyfestivities</p>
  </div>
</section>

<!-- Inside of the trifold -->
<section class="sheet sheet--inside">

  <div class="panel panel--1 pkgs pkgs--light">
    <div class="balloons" role="img" aria-label="Illustration of colourful party balloons"></div>
    <h2 class="pkgs__title hand">Birthday Packages:</h2>
    <p class="pkgs__sub">*Requires Additional Fees</p>
    <div class="pkg">
      <h3 class="pkg__name hand">Basic Birthday <b>($99.99):</b></h3>
      <ul>
        <li>DJ Shout out + Music (to Birthday Boy/Girl including any special requests)</li>
        <li>Confetti (Streamers exploded through confetti cannon)</li>
        <li>One Dozen Balloons/or One Dozen Flowers</li>
        <li>Optional: Gift Presentation</li>
        <li class="note">*Photos/Videos ($5.00 per Photo/$10.00 Video/$49.99 Custom Video)</li>
        <li class="note">*Delivery Method (See Options)</li>
        <li class="note">*Additional instructions (Not Listed, Fees May Vary)</li>
      </ul>
    </div>
    <div class="pkg">
      <h3 class="pkg__name hand">Basic Birthday <b>($99.99):</b></h3>
      <ul>
        <li>DJ Shout out + Music (to Birthday Boy/Girl including any special requests)</li>
        <li>Confetti (Streamers exploded through confetti cannon)</li>
        <li>One Dozen Balloons/or One Dozen Flowers</li>
        <li>Custom Birthday Cookie Cake (Grand Cookie Co.)/ Birthday Sash &amp; Hat or Tiara</li>
        <li>Optional: Gift Presentation</li>
        <li class="note">*Photos/Videos ($5.00 per Photo/$10.00 Video/$49.99 Custom Video)</li>
        <li class="note">*Delivery Method (See Options)</li>
        <li class="note">*Additional Instructions (Not Listed)</li>
      </ul>
    </div>
    <div class="pkg pkg--inset">
      <h3 class="pkg__name hand">Birthday Blowout <b>($199.99):</b></h3>
      <ul>
        <li>DJ Shout out + Music (to Birthday Boy/Girl including any special requests)</li>
        <li>Confetti (Streamers exploded through confetti cannon)</li>
        <li>One Dozen Balloons/ or One Dozen Flowers</li>
        <li>Custom Birthday Cookie Cake (Grand Cookie Co.)</li>
        <li>Birthday Sash &amp; Hat/Tiara</li>
        <li>Free access to all Photos/Videos</li>
        <li>Choice of Delivery Method From Options</li>
        <li>Optional: Gift Presentation</li>
        <li class="note">*Custom Delivery (Not included in Options)</li>
        <li class="note">*Additional instructions (Not Listed)</li>
      </ul>
    </div>
    <svg class="wave" viewBox="0 0 232 120" preserveAspectRatio="none" aria-hidden="true">
      <path d="M0 112 C80 104 170 80 232 50 V120 H0Z" fill="#3a2cd4"/>
      <path d="M0 104 C80 96 170 72 232 40 V48 C170 80 80 102 0 110Z" fill="#4fd0ff"/>
    </svg>
    <div class="photo" style="left:74px;top:414px;width:156px;height:156px;background:linear-gradient(140deg,#ff9a3c,#ffd6a0 45%,#d23a8a)" role="img" aria-label="Photo of friends celebrating a birthday with cake and drinks"></div>
  </div>

  <div class="panel panel--2 pkgs pkgs--dark">
    <h2 class="pkgs__title hand">Anniversary packages</h2>
    <p class="pkgs__sub">*Requires Additional Fees</p>
    <div class="pkg">
      <h3 class="pkg__name hand">Basic Aniversary <b>($99.99):</b></h3>
      <ul>
        <li>DJ Shout out + Music (to significant other including any special requests)</li>
        <li>Confetti/Rose petal confetti (Streamers exploded through confetti cannon)</li>
        <li>One Dozen Balloons/or One Dozen Flowers</li>
        <li>Optional: Gift Presentation</li>
        <li class="note">*Photos/Videos ($5.00 per Photo/$10.00 Video/$49.99 Custom Video)</li>
        <li class="note">*Delivery Method (See Options)</li>
        <li class="note">*Additional instructions (Not Listed, Fees May Vary)</li>
      </ul>
    </div>
    <div class="pkg">
      <h3 class="pkg__name hand">Better Anniversary <b>($124.99):</b></h3>
      <ul>
        <li>DJ Shout out + Music (to significant other including any special requests)</li>
        <li>Confetti/Rose petal confetti (Streamers exploded through confetti cannon)</li>
        <li>One Dozen Balloons/ or One Dozen Flowers</li>
        <li>Custom Birthday Cookie Cake (Grand Cookie Co.)/ Birthday Sash &amp; Hat or Tiara</li>
        <li>Optional: Gift Presentation</li>
        <li class="note">*Photos/Videos ($5.00 per Photo/$10.00 Video/$49.99 Custom Video)</li>
        <li class="note">*Delivery Method (See Options)</li>
        <li class="note">*Additional Instructions (Not Listed)</li>
      </ul>
    </div>
    <div class="pkg">
      <h3 class="pkg__name hand">Anniversary Blowout <b>($199.99)</b></h3>
      <ul>
        <li>DJ Shout out + Music (to significant other including any special requests)</li>
        <li>Confetti/Rose petal confetti (Streamers exploded through confetti cannon)</li>
        <li>One Dozen Balloons/ or One Dozen Flowers</li>
        <li>Custom Birthday Cookie Cake (Grand Cookie Co.)</li>
        <li>Birthday Sash &amp; Hat/Tiara</li>
        <li>Free access to all Photos/Videos</li>
        <li>Choice of Delivery Method From Options</li>
        <li>Optional: Gift Presentation</li>
        <li class="note">*Custom Delivery (Not included in Options)</li>
        <li class="note">*Additional instructions (Not Listed)</li>
      </ul>
    </div>
    <div class="photo" style="left:32px;top:410px;width:168px;height:168px;border-color:#3b2cd6;background:linear-gradient(140deg,#f4f4f8,#f6b8c8 50%,#c9a27a)" role="img" aria-label="Photo of a gift basket with roses and a present"></div>
    <div class="photo" style="left:140px;top:342px;width:80px;height:80px;border-color:#3b2cd6;background:linear-gradient(140deg,#ffffff,#e0182e 40%,#8a0a1a)" role="img" aria-label="Photo of red roses in a heart-shaped box"></div>
  </div>

  <div class="panel panel--3 pkgs pkgs--light">
    <h2 class="pkgs__title hand">Other Events Packages:</h2>
    <p class="pkgs__kinds hand">including but not limited to:</p>
    <ul class="kinds">
      <li>bachelor/bachelorette parties</li><li>feel good moments</li>
      <li>holiday parties</li><li>embarress your friends/coworkers</li>
      <li>breakups/makeups</li><li>office parties</li>
    </ul>
    <div class="pkg" style="margin-top:12px">
      <h3 class="pkg__name hand">Basic <b>($99.99):</b></h3>
      <ul>
        <li>DJ Shout out + Music (including any special requests)</li>
        <li>Confetti (Streamers exploded through confetti cannon)</li>
        <li>One Dozen Balloons/ or One Dozen Flowers</li>
        <li>Optional: Gift Presentation</li>
        <li class="note">*Photos/Videos ($5.00 per Photo/$10.00 Video/$49.99 Custom Video)</li>
        <li class="note">*Delivery Method (See Options)</li>
        <li class="note">*Additional instructions (Not Listed, Fees May Vary)</li>
      </ul>
    </div>
    <div class="pkg" style="margin-top:10px">
      <h3 class="pkg__name hand">Better <b>($124.99):</b></h3>
      <ul>
        <li>DJ Shout out + Music (to Birthday Boy/Girl including any special requests)</li>
        <li>Confetti (Streamers exploded through confetti cannon)</li>
        <li>One Dozen Balloons/ or One Dozen Flowers</li>
        <li>Custom Birthday Cookie Cake (Grand Cookie Co.)/ Birthday Sash &amp; Hat or Tiara</li>
        <li>Optional: Gift Presentation</li>
        <li class="note">*Photos/Videos ($5.00 per Photo/$10.00 Video/$49.99 Custom Video)</li>
        <li class="note">*Delivery Method (See Options)</li>
        <li class="note">*Additional instructions (Not Listed)</li>
      </ul>
    </div>
    <div class="pkg">
      <h3 class="pkg__name hand">Blowout <b>($199.99)</b></h3>
      <ul>
        <li>DJ Shout out + Music (to Birthday Boy/Girl including any special requests)</li>
        <li>Confetti (Streamers exploded through confetti cannon)</li>
        <li>One Dozen Balloons/ or One Dozen Flowers</li>
        <li>Custom Birthday Cookie Cake (Grand Cookie Co.)</li>
        <li>Birthday Sash &amp; Hat/Tiara</li>
        <li>Free access to all Photos/Videos</li>
        <li>Choice of Delivery Method From Options</li>
        <li>Optional: Gift Presentation</li>
        <li class="note">*Custom Delivery (Not included in Options)</li>
        <li class="note">*Additional instructions (Not Listed)</li>
      </ul>
    </div>
    <svg class="wave" viewBox="0 0 232 120" preserveAspectRatio="none" aria-hidden="true">
      <path d="M0 50 C70 70 160 100 232 108 V120 H0Z" fill="#3a2cd4"/>
      <path d="M0 40 C70 62 160 92 232 100 V106 C160 98 70 70 0 48Z" fill="#4fd0ff"/>
    </svg>
    <div class="photo" style="left:38px;top:412px;width:150px;height:150px;background:linear-gradient(140deg,#1a1a3a,#c23a8a 50%,#3a2a6a)" role="img" aria-label="Photo of a crowd dancing at a night party"></div>
    <div class="photo" style="left:140px;top:372px;width:74px;height:74px;border-color:#4fd0ff;background:linear-gradient(140deg,#3a6ad8,#e0a0d0 55%,#4a2ab0)" role="img" aria-label="Photo of masked friends at a costume party"></div>
  </div>
</section>

</body>
</html>
```